Start up in business consultancy needs a business card

We need the business card's layout (we have already the logo). Our business is concerned on consultancy services delivered to companies on the matter of sustainability. Business card should be enough essentials and professional style.

Side A with the following info:
logo + a space for the claim (still to identify) + website of the company

Side B with the following info:
Name of business card holder + title of the business card holder + address of the company + space for mobile number, phone number, fax number + e-mail of business card holder + graphic details around.

Target Market(s)

Business of any sector

Industry/Entity Type

Business Service

Contact Information for Business Card

Name of the company:
Lumeroca srl
Società Benefit

Address of the company:
Via Pescoli, 7
21099 - Castelmira (CM)

Website:
www.lumeroca-esempio.it

Name of the BC' holder:
Ettore Valsenzi

Title:
Co-fondatore

Email:
ettore@lumeroca-esempio.it

Mobile:
+39 351 602 7415
Phone:
+39 351 602 7415
Fax:
+39 351 602 7415

Font styles to use
Other font styles liked:
• new gothic

```html
<!DOCTYPE html>
<html lang="it">
<head>
<meta charset="utf-8">
<title>Lumeroca – biglietto da visita</title>
<link rel="stylesheet" href="https://fonts.googleapis.com/css2?family=Mulish:wght@400;600;700&family=Questrial&family=Source+Sans+3:wght@400;600&display=swap">
<style>
  :root {
    --brand-blue: #0a66a8;
    --ink: #4a4a4a;
    --paper: #ffffff;
    --backdrop: #e6e7e9;
  }
  * { box-sizing: border-box; margin: 0; padding: 0; }
  html, body { width: 1200px; height: 987px; overflow: hidden; }
  body { background: var(--backdrop); position: relative; font-family: "Source Sans 3", sans-serif; }

  .card {
    position: absolute;
    left: 293px;
    width: 615px;
    height: 350px;
    box-shadow: 0 2px 8px rgba(0,0,0,0.18);
  }
  .card--front { top: 130px; background: var(--paper); }
  .card--back { top: 506px; background: var(--brand-blue); }

  /* front */
  .wordmark {
    position: absolute;
    left: 0; right: 0; top: 45px;
    display: flex; justify-content: center; align-items: center; gap: 16px;
  }
  .wordmark__dot {
    width: 102px; height: 102px; border-radius: 50%;
    border: 5px solid var(--brand-blue);
  }
  .wordmark__name {
    font-family: "Mulish", sans-serif; font-weight: 600;
    font-size: 42px; color: var(--brand-blue); letter-spacing: -0.5px;
  }
  .holder {
    position: absolute; top: 194px; left: 43px; right: 41px;
    display: flex; align-items: center; gap: 8px;
  }
  .holder__rule { flex: 1; height: 2px; background: var(--brand-blue); }
  .holder__name {
    font-family: "Mulish", sans-serif; font-weight: 700;
    font-size: 22px; color: var(--brand-blue);
  }
  .holder__title {
    font-family: "Questrial", sans-serif; font-size: 18px; color: var(--ink);
  }
  .company {
    position: absolute; left: 42px; top: 230px;
    font-style: normal;
    font-size: 16.5px; line-height: 23.4px; color: var(--ink);
  }
  .company__name { font-weight: 600; }
  .contacts {
    position: absolute; right: 40px; top: 230px;
    list-style: none; font-size: 16.5px; line-height: 23.4px; color: var(--ink);
  }
  .contacts li { display: flex; justify-content: flex-end; align-items: center; gap: 9px; }
  .contacts svg { width: 15px; height: 15px; fill: var(--brand-blue); flex: none; }

  /* back */
  .emblem {
    position: absolute; left: 50%; top: 168px;
    transform: translate(-50%, -50%);
    width: 180px; height: 180px; border-radius: 50%;
    border: 7px solid var(--paper);
    display: flex; align-items: center; justify-content: center;
  }
  .emblem__name {
    font-family: "Mulish", sans-serif; font-weight: 600;
    font-size: 30px; color: var(--paper);
  }
  .website {
    position: absolute; left: 0; right: 0; top: 290px;
    text-align: center; color: var(--paper);
    font-family: "Source Sans 3", sans-serif; font-size: 16px; letter-spacing: 3px;
  }
</style>
</head>
<body>

<section class="card card--front">
  <div class="wordmark">
    <span class="wordmark__dot"></span>
    <span class="wordmark__name">lumeroca</span>
  </div>

  <div class="holder">
    <span class="holder__rule"></span>
    <span class="holder__name">Ettore Valsenzi -</span>
    <span class="holder__title">Co-fondatore</span>
    <span class="holder__rule"></span>
  </div>

  <address class="company">
    <div class="company__name">Lumeroca srl</div>
    <div>Società Benefit</div>
    <div>Via Pescoli, 7</div>
    <div>21099 - Castelmira (CM)</div>
  </address>

  <ul class="contacts">
    <li>+39 351 602 7415
      <svg viewBox="0 0 24 24" aria-label="telefono"><path d="M6.6 10.8a15.1 15.1 0 0 0 6.6 6.6l2.2-2.2c.3-.3.7-.4 1-.2 1.1.4 2.3.6 3.6.6.6 0 1 .4 1 1V20c0 .6-.4 1-1 1A17 17 0 0 1 3 4c0-.6.4-1 1-1h3.5c.6 0 1 .4 1 1 0 1.3.2 2.5.6 3.6.1.3 0 .7-.2 1z"/></svg>
    </li>
    <li>+39 351 602 7415
      <svg viewBox="0 0 24 24" aria-label="cellulare"><path d="M7 1h10a2 2 0 0 1 2 2v18a2 2 0 0 1-2 2H7a2 2 0 0 1-2-2V3a2 2 0 0 1 2-2zm0 3v15h10V4zm5 16.2a.9.9 0 1 0 0 1.8.9.9 0 0 0 0-1.8z"/></svg>
    </li>
    <li>+39 351 602 7415
      <svg viewBox="0 0 24 24" aria-label="fax"><path d="M6 2h9l3 3v5H6zM3 11h18a1 1 0 0 1 1 1v7a1 1 0 0 1-1 1h-2v2H5v-2H3a1 1 0 0 1-1-1v-7a1 1 0 0 1 1-1zm4 6v3h10v-3z"/></svg>
    </li>
    <li>ettore@lumeroca-esempio.it
      <svg viewBox="0 0 24 24" aria-label="e-mail"><path d="M2 5h20v2.2l-10 6-10-6zm0 4.6 10 6 10-6V19H2z"/></svg>
    </li>
  </ul>
</section>

<section class="card card--back">
  <div class="emblem"><span class="emblem__name">lumeroca</span></div>
  <div class="website">www.lumeroca-esempio.it</div>
</section>

</body>
</html>
```